Fernbrook premium pontoon cleaning and maintenance needs a business card design

we need a business card for a new company based in Brisbane and gold coast that offers to clean peoples pontoons using high pressure washers. The company name will be Fernbrook, and will offer premium pontoon cleaning and maintenance.
colours that can be used maybe black, lime green, grey, blue.but up for anything. cheers

Target Market(s)

people who own pontoons

Industry/Entity Type

Business

Contact Information for Business Card

contact
Rob Calloway
Declan Moss
mobile 0471 628 093
email Fernbrook@mailcove.com

Requirements
Nice to have
• like the look of black business cards the best

```html
<!DOCTYPE html>
<html lang="en">
<head>
<meta charset="utf-8">
<title>Fernbrook Business Card</title>
<link href="https://fonts.googleapis.com/css2?family=Open+Sans:wght@400;700&display=swap" rel="stylesheet">
<style>
  :root {
    --backdrop: #2e2e2e;
    --card-black: #050505;
    --ink-white: #ffffff;
    --ink-soft: #e6e6e6;
    --divider: #8a8a8a;
    --accent-blue: #2f8fd8;
  }
  * { margin: 0; padding: 0; box-sizing: border-box; }
  html, body {
    width: 1200px;
    height: 900px;
    overflow: hidden;
    background: var(--backdrop);
    font-family: "Open Sans", Arial, sans-serif;
  }
  .canvas {
    position: relative;
    width: 1200px;
    height: 900px;
  }
  .card {
    position: absolute;
    left: 280px;
    width: 640px;
    height: 366px;
    background: var(--card-black);
    box-shadow: 0 10px 30px rgba(0,0,0,0.45);
  }
  .card--front { top: 70px; display: flex; align-items: center; justify-content: center; }
  .card--back { top: 464px; display: flex; align-items: center; padding-left: 78px; }

  .wordmark {
    color: var(--ink-white);
    font-weight: 700;
    letter-spacing: 4px;
    text-transform: uppercase;
    line-height: 1;
  }
  .card--front .wordmark { font-size: 62px; }
  .card--back .wordmark { font-size: 40px; letter-spacing: 3px; }

  .divider {
    width: 1px;
    height: 112px;
    background: linear-gradient(to bottom, transparent, var(--divider) 20%, var(--divider) 80%, transparent);
    margin: 0 16px 0 22px;
  }
  .contact { color: var(--ink-white); }
  .contact__names {
    font-weight: 700;
    font-size: 17px;
    line-height: 1.2;
    text-transform: uppercase;
    margin-bottom: 8px;
  }
  .contact__line {
    display: flex;
    align-items: center;
    gap: 7px;
    font-size: 14px;
    line-height: 1.35;
    color: var(--ink-soft);
  }
  .contact__icon { width: 11px; height: 11px; flex: none; }
</style>
</head>
<body>
<div class="canvas">
  <section class="card card--front">
    <div class="wordmark">Fernbrook</div>
  </section>

  <section class="card card--back">
    <div class="wordmark">Fernbrook</div>
    <div class="divider"></div>
    <div class="contact">
      <div class="contact__names">
        <div>Rob Calloway</div>
        <div>Declan Moss</div>
      </div>
      <div class="contact__line">
        <svg class="contact__icon" viewBox="0 0 12 12" aria-hidden="true">
          <rect x="3" y="0.8" width="6" height="10.4" rx="1" fill="none" stroke="var(--accent-blue)" stroke-width="1.3"/>
          <line x1="5" y1="9.3" x2="7" y2="9.3" stroke="var(--accent-blue)" stroke-width="1"/>
        </svg>
        <span>0471 628 093</span>
      </div>
      <div class="contact__line">
        <svg class="contact__icon" viewBox="0 0 12 12" aria-hidden="true">
          <rect x="0.8" y="2.2" width="10.4" height="7.6" fill="none" stroke="var(--accent-blue)" stroke-width="1.3"/>
          <polyline points="0.8,2.4 6,6.6 11.2,2.4" fill="none" stroke="var(--accent-blue)" stroke-width="1.2"/>
        </svg>
        <span>Fernbrook@mailcove.com</span>
      </div>
    </div>
  </section>
</div>
</body>
</html>
```